Business cards for financial advisor-insurance agent firm

Our company, Harlow Pemberton Insurance & Investments, is an insurance (health, life, home, auto, etc) and investment brokerage offering a suite of options to meet client needs. We need business cards that are professional and embody strength, security and sophistication.

Also running a letterhead project at
http://jobs.briefmarlo.com/job.aspx?id=519087

Target Market(s)

Upper middle class and wealthy

Industry/Entity Type

Investment

Requirements
Nice to have
• Looking for either white, navy blue, or gray cards

```html
<!DOCTYPE html>
<html lang="en">
<head>
<meta charset="utf-8">
<title>Harlow Pemberton Insurance &amp; Investments – Business Cards</title>
<link rel="stylesheet" href="https://fonts.googleapis.com/css2?family=Cinzel:wght@400;600&family=Open+Sans:wght@600;700&display=swap">
<style>
  :root {
    --backdrop: #1f1f21;
    --navy: #2d3768;
    --navy-deep: #252e5a;
    --paper-glow: #f2f2f4;
    --paper-mid: #c4c4ca;
    --paper-edge: #8e8f98;
    --mist: #c3c7da;
    --bar-light: rgba(200, 206, 228, 0.32);
  }
  * { margin: 0; padding: 0; box-sizing: border-box; }
  html, body {
    width: 1200px;
    height: 899px;
    overflow: hidden;
    background: var(--backdrop);
  }
  .stage {
    position: relative;
    width: 1200px;
    height: 899px;
  }
  .card {
    position: absolute;
    top: 300px;
    width: 520px;
    height: 298px;
    overflow: hidden;
    box-shadow: 0 14px 30px rgba(0, 0, 0, 0.55);
  }

  /* Back card: light grey */
  .card--back {
    left: 50px;
    background: radial-gradient(ellipse 60% 55% at 58% 52%, var(--paper-glow) 0%, var(--paper-mid) 55%, var(--paper-edge) 100%);
  }
  .card--back .stripes {
    position: absolute;
    top: 0;
    left: 432px;
    display: flex;
    gap: 9px;
  }
  .card--back .stripe {
    width: 9px;
    height: 120px;
    background: var(--navy);
  }
  .card--back .stripe:first-child { width: 10px; height: 140px; }
  .holder {
    position: absolute;
    top: 34px;
    right: 110px;
    text-align: right;
    color: #ffffff;
    font-family: "Open Sans", sans-serif;
  }
  .holder__name { font-size: 18px; font-weight: 700; letter-spacing: 0.5px; }
  .holder__role { font-size: 11px; font-weight: 700; letter-spacing: 0.3px; }
  .card--back .brand {
    position: absolute;
    left: 36px;
    bottom: 50px;
  }
  .card--back .brand__mark {
    width: 40px;
    height: 40px;
    border: 2px solid var(--navy);
    margin-bottom: 8px;
  }
  .card--back .brand__name,
  .card--back .brand__line {
    font-family: "Cinzel", serif;
    font-weight: 600;
    color: #ffffff;
    line-height: 1.15;
  }
  .card--back .brand__name { font-size: 20px; letter-spacing: 0.5px; }
  .card--back .brand__line { font-size: 11px; letter-spacing: 0.6px; }

  /* Front card: navy */
  .card--front {
    left: 630px;
    background: radial-gradient(circle at 22% 78%, #3d4780 0%, var(--navy) 18%, var(--navy) 60%, var(--navy-deep) 100%);
  }
  .bar {
    position: absolute;
    background: var(--bar-light);
  }
  .bar--right-a { left: 440px; top: 0; width: 14px; height: 298px; }
  .bar--right-b { left: 466px; top: 0; width: 14px; height: 200px; }
  .bar--left-a  { left: 24px;  top: 20px; width: 12px; height: 54px; }
  .bar--left-b  { left: 44px;  top: 20px; width: 12px; height: 70px; }
  .card--front .brand {
    position: absolute;
    left: 60px;
    width: 360px;
    top: 70px;
    text-align: center;
  }
  .card--front .brand__mark {
    display: block;
    width: 76px;
    height: 76px;
    margin: 0 auto 16px;
    border: 3px solid var(--mist);
  }
  .card--front .brand__name,
  .card--front .brand__line {
    font-family: "Cinzel", serif;
    font-weight: 400;
    color: var(--mist);
    line-height: 1.15;
    white-space: nowrap;
  }
  .card--front .brand__name { font-size: 29px; letter-spacing: 0.5px; }
  .card--front .brand__line { font-size: 15px; letter-spacing: 0.8px; }
</style>
</head>
<body>
<main class="stage">
  <section class="card card--back" aria-label="Business card, contact side">
    <div class="stripes">
      <span class="stripe"></span>
      <span class="stripe"></span>
    </div>
    <div class="holder">
      <p class="holder__name">Miles Avery</p>
      <p class="holder__role">General Manager</p>
    </div>
    <div class="brand">
      <div class="brand__mark"></div>
      <p class="brand__name">Harlow Pemberton</p>
      <p class="brand__line">Insurance &amp; Investments</p>
    </div>
  </section>

  <section class="card card--front" aria-label="Business card, brand side">
    <span class="bar bar--left-a"></span>
    <span class="bar bar--left-b"></span>
    <span class="bar bar--right-a"></span>
    <span class="bar bar--right-b"></span>
    <div class="brand">
      <span class="brand__mark"></span>
      <p class="brand__name">Harlow Pemberton</p>
      <p class="brand__line">Insurance &amp; Investments</p>
    </div>
  </section>
</main>
</body>
</html>
```